Brightwave Travel and Tours

Hotel Reservations
Airline Ticketing
Day Tour

My business is a Travel agency. My services are issuing domestic and international tickets. Book room/hotel reservations local/international.
My color preference is apple green/orange/red/blue.
Images of beaches, tickets,luggage.

```html
<!DOCTYPE html>
<html lang="en">
<head>
<meta charset="utf-8">
<title>Brightwave Travel and Tours – Business Card</title>
<link rel="stylesheet" href="https://fonts.googleapis.com/css2?family=Open+Sans:ital,wght@0,400;0,600;0,700;1,400&display=swap">
<style>
  :root {
    --page-bg: #e9ecee;
    --card-frost: #f4f7f8;
    --card-frost-edge: #e2e9ec;
    --teal-light: #7fe0ea;
    --teal-mid: #2fb8c8;
    --teal-deep: #178596;
    --accent-red: #d9401f;
    --accent-orange: #f08a1c;
    --brand-teal: #2b6d80;
    --ink-navy: #14365a;
    --ink-dark: #1d2a35;
    --ink-grey: #55636d;
  }
  * { margin: 0; padding: 0; box-sizing: border-box; }
  html, body { width: 1200px; height: 969px; overflow: hidden; }
  body {
    background: var(--page-bg);
    font-family: "Open Sans", Arial, sans-serif;
    position: relative;
  }
  .business-card {
    position: absolute;
    left: 100px;
    top: 202px;
    width: 1000px;
    height: 564px;
    border-radius: 28px;
    overflow: hidden;
    background: linear-gradient(160deg, var(--card-frost) 0%, var(--card-frost-edge) 100%);
    box-shadow: 0 18px 40px rgba(20, 40, 55, 0.18);
  }
  .card-shapes { position: absolute; inset: 0; }
  .brand-block {
    position: absolute;
    left: 40px;
    width: 520px;
    top: 70px;
    text-align: center;
  }
  .brand-mark {
    width: 120px;
    height: 120px;
    border-radius: 50%;
    background: var(--teal-mid);
    margin: 0 auto 34px;
  }
  .brand-name {
    font-weight: 700;
    font-size: 40px;
    line-height: 46px;
    color: var(--brand-teal);
    letter-spacing: 1px;
    text-transform: uppercase;
  }
  .service-list {
    list-style: none;
    margin-top: 22px;
    font-style: italic;
    font-size: 23px;
    color: var(--ink-grey);
    line-height: 38px;
  }
  .service-list li { display: inline-block; margin: 0 10px; }
  .service-list li::before {
    content: "";
    display: inline-block;
    width: 9px; height: 9px;
    border-radius: 50%;
    background: var(--accent-orange);
    margin-right: 9px;
    vertical-align: middle;
  }
  .contact-block {
    position: absolute;
    right: 40px;
    top: 60px;
    text-align: right;
    color: var(--ink-dark);
  }
  .person-name { font-size: 34px; font-weight: 600; color: var(--ink-navy); line-height: 42px; }
  .person-title { font-size: 24px; color: var(--ink-navy); line-height: 32px; }
  .address { margin-top: 48px; font-size: 22px; line-height: 33px; }
  .contact-lines { margin-top: 28px; list-style: none; font-size: 22px; line-height: 34px; }
  .contact-lines li { display: flex; justify-content: flex-end; align-items: center; gap: 18px; }
  .contact-lines svg { width: 22px; height: 22px; fill: var(--ink-navy); flex: none; }
</style>
</head>
<body>
  <div class="business-card">
    <svg class="card-shapes" width="1000" height="564" viewBox="0 0 1000 564" aria-hidden="true">
      <defs>
        <linearGradient id="tealPanel" x1="0" y1="0" x2="1" y2="1">
          <stop offset="0" stop-color="var(--teal-light)"/>
          <stop offset="0.5" stop-color="var(--teal-mid)"/>
          <stop offset="1" stop-color="var(--teal-deep)"/>
        </linearGradient>
        <radialGradient id="palmGlow" cx="0.5" cy="0.5" r="0.5">
          <stop offset="0" stop-color="#ffffff" stop-opacity="0.45"/>
          <stop offset="1" stop-color="#ffffff" stop-opacity="0"/>
        </radialGradient>
      </defs>
      <path d="M436 0 C 560 90, 600 330, 373 564 L1000 564 L1000 0 Z" fill="url(#tealPanel)"/>
      <path d="M436 0 C 560 90, 600 330, 373 564" fill="none" stroke="var(--accent-red)" stroke-width="9"/>
    </svg>
    <svg class="card-shapes" width="1000" height="564" viewBox="0 0 1000 564" role="img" aria-label="Faint palm tree silhouette decoration">
      <ellipse cx="440" cy="200" rx="110" ry="140" fill="url(#palmGlow)"/>
    </svg>

    <div class="brand-block">
      <div class="brand-mark"></div>
      <div class="brand-name">Brightwave<br>Travel and Tours</div>
      <ul class="service-list">
        <li>Hotel Reservations</li><li>Airline Ticketing</li><br><li>Day Tour</li>
      </ul>
    </div>

    <div class="contact-block">
      <div class="person-name">Daniel Reyes</div>
      <div class="person-title">CEO/Founder</div>
      <div class="address">2140 Harbor View Road<br>Seaside, Oregon 97138</div>
      <ul class="contact-lines">
        <li>503 218 4471
          <svg viewBox="0 0 24 24"><path d="M6.6 10.8a15.1 15.1 0 0 0 6.6 6.6l2.2-2.2a1 1 0 0 1 1-.25 11.4 11.4 0 0 0 3.6.57 1 1 0 0 1 1 1V20a1 1 0 0 1-1 1A17 17 0 0 1 3 4a1 1 0 0 1 1-1h3.5a1 1 0 0 1 1 1c0 1.25.2 2.45.57 3.57a1 1 0 0 1-.25 1z"/></svg></li>
        <li>503 729 6185
          <svg viewBox="0 0 24 24"><path d="M7 1h10a2 2 0 0 1 2 2v18a2 2 0 0 1-2 2H7a2 2 0 0 1-2-2V3a2 2 0 0 1 2-2zm0 3v15h10V4zm5 16.2a1 1 0 1 0 0 2 1 1 0 0 0 0-2z"/></svg></li>
        <li>503 640 2297
          <svg viewBox="0 0 24 24"><path d="M6 2h12v5H6zM4 8h16a2 2 0 0 1 2 2v7h-4v5H6v-5H2v-7a2 2 0 0 1 2-2zm4 7v5h8v-5z"/></svg></li>
        <li>hello@brightwave.travel
          <svg viewBox="0 0 24 24"><path d="M2 5h20v14H2zm2 2v.5l8 5 8-5V7zm0 2.8V17h16V9.8l-8 5z"/></svg></li>
        <li>www.brightwave.travel
          <svg viewBox="0 0 24 24"><path d="M12 2a10 10 0 1 0 0 20 10 10 0 0 0 0-20zm-1 17.9A8 8 0 0 1 4.2 10.3L9 15v1a2 2 0 0 0 2 2zm6.9-2.5A2 2 0 0 0 16 16h-1v-3a1 1 0 0 0-1-1H8v-2h2a1 1 0 0 0 1-1V7h2a2 2 0 0 0 2-2v-.4a8 8 0 0 1 2.9 12.8z"/></svg></li>
      </ul>
    </div>
  </div>
</body>
</html>
```